Business Card & Word Docs from existing Logo

We need a business card with typical information plus layout to include electrical contractors license number, VORLE license and KMT license. We would like a word document layout for a proposal document, opening page with logo and design basic information; proposal to and proposal from and project name and number. Small basic single page letter for general documents. Email signature with logo.

We are an electrical, refrigeration and automation contractor. We work with reducing energy consumption for our customers and complex process solutions in electrical, refrigeration and automation.
Updates

Reason: Final changes/ revisions to designs.

Target Market(s)

Industrial and commercial businesses that require more than your average contractor.

Industry/Entity Type

Electrical

Requirements
Must have
• Propsal document must have a full opening page.

```html
<!DOCTYPE html>
<html lang="en">
<head>
<meta charset="utf-8">
<title>NorthCool Contracting – Letterhead</title>
<link href="https://fonts.googleapis.com/css2?family=Questrial&display=swap" rel="stylesheet">
<style>
  :root {
    --paper: #ffffff;
    --text-blue: #3b8cc6;
    --navy: #183c66;
    --teal: #1d9bb2;
    --green: #4dab4f;
  }
  html, body { margin: 0; padding: 0; overflow: hidden; }
  body { width: 900px; height: 1200px; background: var(--paper); font-family: 'Questrial', sans-serif; }
  .letterhead { position: relative; width: 900px; height: 1200px; overflow: hidden; background: var(--paper); }
  .sender-details {
    position: absolute; right: 376px; top: 26px; margin: 0;
    text-align: right; color: var(--text-blue); font-size: 15px; line-height: 23px; font-style: normal;
  }
  .header-rule { position: absolute; left: 530px; top: 36px; width: 2px; height: 92px; background: var(--green); }
  .brand { position: absolute; left: 556px; top: 36px; display: flex; align-items: center; gap: 14px; }
  .brand-dot { width: 58px; height: 58px; border-radius: 50%; background: var(--teal); flex: none; }
  .brand-name { color: var(--teal); font-size: 30px; line-height: 30px; letter-spacing: 1px; }
  .brand-name span { display: block; font-size: 17px; line-height: 24px; letter-spacing: 7px; }
  .phone-list {
    position: absolute; right: 50px; top: 108px; margin: 0; padding: 0; list-style: none;
    text-align: right; color: var(--navy); font-size: 13px; line-height: 15px;
  }
  .date-line { position: absolute; left: 658px; top: 178px; color: var(--text-blue); font-size: 19px; }
  .field { position: absolute; left: 90px; margin: 0; color: var(--text-blue); font-size: 19px; line-height: 26px; }
  .recipient { top: 258px; }
  .salutation { top: 406px; }
  .body-text { top: 538px; }
  .closing { top: 840px; }
  .regards { top: 916px; }
  .signature { top: 984px; }
  .footer-band {
    position: absolute; left: 0; right: 0; bottom: 0; height: 42px; background: var(--navy);
    display: flex; align-items: center; justify-content: flex-end; padding-right: 12px;
  }
  .website { color: #ffffff; font-size: 19px; letter-spacing: 19.5px; }
  .corner-mark { position: absolute; left: 4px; top: 1090px; }
</style>
</head>
<body>
<main class="letterhead">
  <address class="sender-details">
    PO Box 5678, Tarrow, Queensland, 4999<br>
    E-mail: sam@northcool.com.au<br>
    Electrical Contractors License 67890<br>
    KMT 1234567<br>
    VORLE AA12345
  </address>
  <div class="header-rule"></div>
  <div class="brand">
    <div class="brand-dot"></div>
    <div class="brand-name">NORTHCOOL<span>CONTRACTING</span></div>
  </div>
  <ul class="phone-list">
    <li>T: 07 5550 1010</li>
    <li>F: 07 5550 1011</li>
    <li>M: 0400 555 212</li>
  </ul>
  <div class="date-line">Date: .................</div>

  <p class="field recipient">Proposal to<br>Name:<br>Address:</p>
  <p class="field salutation">Salutation</p>
  <p class="field body-text">Body Text</p>
  <p class="field closing">Closing "call to action"</p>
  <p class="field regards">Best regards</p>
  <p class="field signature">Signature<br>(Sender's name)</p>

  <div class="footer-band"><span class="website">www.northcool.com.au</span></div>
  <svg class="corner-mark" width="136" height="110" viewBox="0 0 136 110" aria-hidden="true">
    <circle cx="66" cy="68" r="62" fill="var(--teal)"/>
  </svg>
</main>
</body>
</html>
```